Davit Catalog

We need a catalog and possible up to 8 total to describe the equipment we provide. The davit system is one piece to suspending workers on the sides of buildings. The final design should show pictures and engineered details of the davit systems we supply along with photos for reference. Must be better than competitors!

Target Market(s)

architects, general contractors

Industry/Entity Type

Window Cleaning

Colors
0455a3
ec1f27
ffffff

```html
<!DOCTYPE html>
<html lang="en">
<head>
<meta charset="utf-8">
<title>Davit Catalog – Spread</title>
<link href="https://fonts.googleapis.com/css2?family=Open+Sans:ital,wght@0,400;0,600;0,700;1,400&display=swap" rel="stylesheet">
<style>
  :root {
    --brand-blue: #0455a3;
    --brand-red: #ec1f27;
    --paper: #ffffff;
    --page-tint: #f6f6f6;
    --ink: #2b2b2b;
    --backdrop: #e9e7e3;
  }
  * { box-sizing: border-box; margin: 0; padding: 0; }
  html, body {
    width: 1200px; height: 880px; overflow: hidden;
    background: var(--backdrop);
    font-family: "Open Sans", Arial, sans-serif;
    color: var(--ink);
  }
  .spread {
    position: absolute; left: 40px; top: 243px;
    width: 1120px; height: 394px;
    display: grid; grid-template-columns: repeat(4, 1fr);
    box-shadow: 0 10px 30px rgba(0,0,0,.18);
    background: var(--paper);
  }
  .page-text {
    background: var(--page-tint);
    padding: 22px 20px;
    font-size: 8.6px; line-height: 1.42;
  }
  .page-text p { text-align: justify; margin-bottom: 11px; }
  .intro { font-style: italic; }
  .inset-photo {
    height: 156px; margin-top: 16px;
    background: linear-gradient(180deg, #8fb3cf 0%, #a9c0d2 55%, #5d6670 100%);
  }
  .full-photo { height: 100%; }
  .photo-rigging { background: linear-gradient(160deg, #3d4045 0%, #6b6f74 45%, #9a9d9f 75%, #cfd2d4 100%); }
  .photo-tower { background: linear-gradient(200deg, #9aa4a8 0%, #c9d0d2 40%, #7d8a8c 70%, #5e4a43 100%); }
  .spine-left { box-shadow: inset -14px 0 18px -12px rgba(0,0,0,.35); }
  .spine-right { box-shadow: inset 14px 0 18px -12px rgba(0,0,0,.25); }
  .spec-title {
    color: var(--brand-red); font-weight: 700; font-size: 10.5px;
    letter-spacing: .02em; margin-bottom: 12px;
  }
  .spec-subtitle { font-weight: 700; font-size: 8.6px; margin-top: 2px; }
  .spec-list { list-style: none; padding-left: 12px; }
  .spec-list li { position: relative; text-align: justify; }
  .spec-list li::before { content: "•"; position: absolute; left: -10px; }
  .spec-note { margin-bottom: 10px; }
</style>
</head>
<body>
  <section class="spread">
    <article class="page-text spine-left-none">
      <p class="intro">The Davit system consists of galvanized steel sockets, anchored to the building and a high-strength aluminium alloy mast and arm (the davit). The davit suspends either a roof-rigged or ground-rigged powered platform with safe access and egress on the roof. HARBORLINE in partnership with LOFTRIG offers a variety of operator-friendly davit systems.</p>
      <p class="intro">Davit systems are implemented nation wide, easy to operate, economical and readily customized. Sockets are generally exposed, but can be recessed below the roof surface where public space requires an aesthetic solution. Sockets and davits offer the advantage of allowing maintenance personnel to board the stage while it rests on the rooftop and can be designed to work on buildings with multiple levels (terraces, balconies, etc.).</p>
      <div class="inset-photo" role="img" aria-label="Two workers on a suspended platform hung from a rooftop davit, city skyline behind"></div>
    </article>
    <div class="full-photo photo-rigging spine-left" role="img" aria-label="Overhead view of a worker in a harness on a suspended platform beside a building, truck parked below"></div>
    <article class="page-text spine-right">
      <h2 class="spec-title">SPECIFICATIONS</h2>
      <p>The standard Loftrig Portable Davit consists of a vertical mast, horizontal boom and diagonal support brace, which are all fabricated from high strength 6061-T6 extruded aluminum tube and channel. A bearing assembly consisting of a cast aluminum housing and socket system fixed to the building surface. All Loftrig products conform to CSA and OSHA standards.</p>
      <p>The Loftrig Portable Davit is available in 1,000 lb (453.6 kg) and 1,250 lb (567kg) carrying capacities (refer to the load table from Loftrig).</p>
      <h3 class="spec-subtitle">Roof Rigged System (High Profile Davit)</h3>
      <ul class="spec-list">
        <li>The self-powered work platform can be raised above the building face being serviced and transferred inboard for storage, rigging and access or egress from work station.</li>
        <li>The point of suspension exceeds 300ft (91m) above a safe surface.</li>
      </ul>
      <p class="spec-note">Reach does not exceed 7 ft 6 in. (2.2 m).</p>
      <h3 class="spec-subtitle">Ground Rigged System (Low Profile Davit)</h3>
      <ul class="spec-list">
        <li>The building design allows a davit be rigged and erected over a parapet on the rooftop.</li>
        <li>The self-powered work platform is ground rigged and disengaged from the outriggers after each day's use and stored at grade.</li>
      </ul>
      <p class="spec-note">Reach does not exceed 7 ft 6 in. (2.2 m).</p>
    </article>
    <div class="full-photo photo-tower" role="img" aria-label="Aerial view of a glass residential tower beside a waterfront"></div>
  </section>
</body>
</html>
```